Export company based in South America (Ecuador) we export flowers, chocolate, and bananas

We need a website that gives our potential clients and introduction into our company and the different types of commodities we export around the world. We are based in Quito, Ecuador so the website should portray the feel of Ecuadorian landscapes within a modern looking website.
At the moment we are exporting roses, chocolate, and bananas so the website should have an intro to our company and then three different areas that describe our three main commodity. The three different sections should explain why each of the products from Ecuador are some of the best in the world in their categories and the benefits of importing the commodity through our company.
Industry/Entity Type
Commodity
Number of Pages Required
4 page

```html
<!DOCTYPE html>
<html lang="en">
<head>
<meta charset="utf-8">
<title>Mirador — Export Company in South America</title>
<link rel="stylesheet" href="https://fonts.googleapis.com/css2?family=IBM+Plex+Sans:wght@400;500;600;700&family=Poppins:wght@600;800&display=swap">
<style>
:root{
  --red:#ee2f2f;
  --navy:#2c3246;
  --ink:#1d1d1f;
  --text:#555a63;
  --muted:#9a9a9a;
  --bg-soft:#f4f1f1;
  --white:#ffffff;
  --line:#d8d8d8;
}
*{box-sizing:border-box;margin:0;padding:0}
html,body{width:1200px;height:3934px;overflow:hidden}
body{font-family:"IBM Plex Sans",Arial,sans-serif;color:var(--ink);background:var(--white);position:relative}
section,header,footer{position:relative;width:1200px}
.abs{position:absolute}
a{color:inherit;text-decoration:none}

/* header */
.site-header{height:112px;background:var(--white)}
.brand-mark{width:76px;height:76px;border-radius:50%;background:var(--red)}
.brand-name{font-weight:600;font-size:33px;letter-spacing:.5px;color:var(--ink)}
.follow{left:672px;top:31px;display:flex;align-items:center;gap:8px;font-size:13px;letter-spacing:.5px}
.follow .dot{width:27px;height:27px;border-radius:50%;background:var(--navy)}
.follow .dot.blue{background:#3a68c4}
.call{left:878px;top:20px;display:flex;gap:12px}
.call small{display:block;font-size:13px;letter-spacing:.5px}
.call strong{display:block;font-size:23px;font-weight:500;color:var(--red);line-height:1.1}
.main-nav{right:131px;top:77px;display:flex;gap:34px;font-size:15px;font-weight:600}
.main-nav .active{color:var(--red);border-bottom:2px solid var(--red)}

/* hero */
.hero{height:502px;background:linear-gradient(180deg,#d87a52 0%,#b0546a 28%,#4b3a4f 55%,#2a2430 78%,#3a2e2c 100%)}
.hero-title{width:100%;top:70px;text-align:center;font-family:"Poppins",Arial,sans-serif;font-weight:800;font-size:46px;line-height:54px;color:var(--white);text-shadow:0 2px 6px rgba(0,0,0,.35)}
.btn{display:inline-block;background:var(--red);color:var(--white);font-weight:600;text-transform:uppercase}
.hero .btn{left:530px;top:199px;width:139px;height:42px;line-height:38px;text-align:center;font-size:16px;border:2px solid rgba(255,255,255,.8)}
.hero-dots{top:445px;width:100%;display:flex;justify-content:center;gap:14px;align-items:center}
.hero-dots i{width:9px;height:9px;border-radius:50%;background:var(--white)}
.hero-dots i.on{width:14px;height:14px;background:var(--red);border:2px solid var(--white)}

/* welcome */
.welcome{height:490px;background:linear-gradient(180deg,#ececec 0%,#e2e2e2 50%,#eeeeee 100%)}
.welcome-kicker{left:130px;top:52px;font-size:23px;font-weight:500}
.welcome-title{left:130px;top:80px;font-size:38px;font-weight:700;letter-spacing:.5px}
.welcome-frame{left:131px;top:143px;width:564px;height:284px;border:3px solid #a9a9a9}
.welcome-text{left:173px;top:178px;width:335px;font-size:13px;line-height:19.2px;color:#333}
.btn.small{font-size:12px;height:29px;line-height:29px;padding:0 13px}
.welcome .btn{left:177px;top:365px;border:1px solid #fff;outline:1px solid var(--red)}
.welcome-photo{left:573px;top:72px;width:494px;height:296px;background:linear-gradient(160deg,#6f98cf 0%,#8aa4b8 30%,#7d6a55 50%,#2fa6a3 70%,#7da44a 100%)}

/* section headings */
.section-title{width:100%;text-align:center;font-size:27px;font-weight:600;letter-spacing:.5px}
.section-rule{left:572px;width:56px;height:2px;background:var(--muted)}

/* products */
.products{height:1390px;background:var(--bg-soft)}
.product-photo{width:592px;height:353px}
.photo-flowers{background:radial-gradient(circle at 45% 50%,#f07a4e 0%,#e2583a 28%,#3f6b2b 52%,#1f3a18 100%)}
.photo-chocolate{background:radial-gradient(circle at 50% 50%,#7a4a36 0%,#4d2a1d 55%,#2d1710 100%)}
.photo-bananas{background:linear-gradient(135deg,#f3d34a 0%,#e8c232 40%,#c79d1e 70%,#f2d75c 100%)}
.product-card{width:434px;height:281px;background:var(--white);box-shadow:0 10px 28px rgba(0,0,0,.13);padding:40px 30px 0 37px}
.product-card h3{font-size:22px;font-weight:600;letter-spacing:.5px;margin-bottom:14px}
.product-card p{font-size:12.6px;line-height:17.6px;color:var(--text)}
.product-card .btn{margin-top:22px;font-size:11.5px;height:29px;line-height:29px;padding:0 13px}

/* why */
.why{height:571px;background:var(--white)}
.feature{width:200px}
.feature h4{font-size:13px;font-weight:600;letter-spacing:.4px;margin-bottom:4px}
.feature p{font-size:12.6px;line-height:16.5px;color:var(--text)}
.feature-icon{width:69px;height:69px;border-radius:50%;background:var(--navy);display:flex;align-items:center;justify-content:center}
.globe{left:455px;top:194px;width:290px;height:290px;border-radius:50%;background:radial-gradient(circle at 40% 35%,#ffffff 0%,#cfdff0 35%,#7ea6cf 70%,#5f87b4 100%)}

/* benefits */
.benefits{height:467px;background:var(--bg-soft)}
.benefit-list{left:129px;top:142px;display:flex;gap:12px}
.benefit-card{width:227px;height:271px;background:var(--white);border:1px solid var(--line);text-align:center;padding:30px 18px 0}
.benefit-card svg{width:64px;height:60px}
.benefit-card h4{margin-top:26px;font-size:13.5px;font-weight:700;letter-spacing:.3px}
.benefit-card p{margin-top:10px;font-size:12px;line-height:16px;color:var(--text)}

/* footer */
.site-footer{height:402px;background:var(--navy);color:var(--white)}
.site-footer .brand-mark{width:70px;height:70px}
.footer-col h5{font-size:16px;font-weight:600;letter-spacing:.5px;margin-bottom:20px}
.footer-menu li{list-style:none;font-size:14px;line-height:24px;letter-spacing:.3px}
.footer-item{display:flex;gap:12px;align-items:flex-start;font-size:14px;line-height:19px;margin-bottom:23px}
.footer-item .ico{flex:none;width:27px;height:27px;border-radius:50%;background:var(--white);display:flex;align-items:center;justify-content:center;margin-top:4px}
.footer-rule{left:130px;top:319px;width:940px;height:1px;background:#4a5064}
.copyright{top:352px;width:100%;text-align:center;font-size:11px;color:#cfd2da}
</style>
</head>
<body>

<header class="site-header">
  <div class="abs brand-mark" style="left:130px;top:23px"></div>
  <div class="abs brand-name" style="left:215px;top:42px">MIRADOR</div>
  <div class="abs follow">FOLLOW <span class="dot blue"></span><span class="dot blue"></span><span class="dot"></span></div>
  <div class="abs call">
    <svg width="32" height="32" viewBox="0 0 24 24" fill="none" stroke="#333" stroke-width="1.6"><path d="M5 3h4l2 5-2.5 1.5a11 11 0 0 0 6 6L16 13l5 2v4a2 2 0 0 1-2 2A16 16 0 0 1 3 5a2 2 0 0 1 2-2z"/><path d="M14 3a7 7 0 0 1 7 7M14 7a3 3 0 0 1 3 3"/></svg>
    <div><small>CALL US</small><strong>555.014.2200</strong></div>
  </div>
  <nav class="abs main-nav">
    <a class="active" href="#">HOME</a><a href="#">ABOUT US</a><a href="#">SERVICES</a><a href="#">BLOG</a><a href="#">CONTACT US</a>
  </nav>
</header>

<section class="hero" role="img" aria-label="Hillside city in Ecuador at sunset with glowing houses and radio towers">
  <h1 class="abs hero-title">EXPORT COMPANY<br>IN SOUTH AMERICA</h1>
  <a class="abs btn" href="#">READ MORE</a>
  <div class="abs hero-dots"><i></i><i></i><i class="on"></i><i></i><i></i></div>
</section>

<section class="welcome">
  <div class="abs welcome-frame"></div>
  <p class="abs welcome-kicker">WELCOME TO</p>
  <h2 class="abs welcome-title">MIRADOR</h2>
  <p class="abs welcome-text">Lorem Ipsum is simply dummy text of the printing and typesetting industry. Lorem Ipsum has been the industry's standard dummy text ever since the 1500s, when an unknown printer took a galley of type and scrambled it to make a type specimen book. It has survived not only five centuries, but also the leap into electronic typesetting, remaining essentially unchanged. It was popularised in the.</p>
  <a class="abs btn small" href="#">READ MORE</a>
  <div class="abs welcome-photo" role="img" aria-label="Volcanic island coastline with turquoise bays and green hills"></div>
</section>

<section class="products">
  <h2 class="abs section-title" style="top:54px">EXPORT PRODUCTS</h2>
  <div class="abs section-rule" style="top:107px"></div>

  <div class="abs product-photo photo-flowers" style="left:130px;top:159px" role="img" aria-label="Orange dahlia flower in bloom with a bud beside it"></div>
  <article class="abs product-card" style="left:638px;top:199px">
    <h3>FLOWERS</h3>
    <p>Sed ut perspiciatis unde omnis iste natus error sit voluptatem accusantium doloremque laudantium, totam rem aperiam, eaque ipsa quae ab illo inventore veritatis et quasi architecto beatae vitae dicta sunt explicabo. Nemo enim ipsam voluptatem quia voluptas sit aspernatur aut odit aut fugit, sed quia consequuntur magni dolores eos qui ratione voluptatem sequi nesciunt.</p>
    <a class="btn" href="#">READ MORE</a>
  </article>

  <div class="abs product-photo photo-chocolate" style="left:475px;top:563px" role="img" aria-label="Assorted filled chocolates and pralines"></div>
  <article class="abs product-card" style="left:130px;top:603px;padding-left:32px">
    <h3>CHOCOLATE</h3>
    <p>Sed ut perspiciatis unde omnis iste natus error sit voluptatem accusantium doloremque laudantium, totam rem aperiam, eaque ipsa quae ab illo inventore veritatis et quasi architecto beatae vitae dicta sunt explicabo. Nemo enim ipsam voluptatem quia voluptas sit aspernatur aut odit aut fugit, sed quia consequuntur magni dolores eos qui ratione voluptatem sequi nesciunt.</p>
    <a class="btn" href="#">READ MORE</a>
  </article>

  <div class="abs product-photo photo-bananas" style="left:130px;top:976px" role="img" aria-label="Pile of ripe yellow bananas"></div>
  <article class="abs product-card" style="left:638px;top:1016px">
    <h3>BANANAS</h3>
    <p>Sed ut perspiciatis unde omnis iste natus error sit voluptatem accusantium doloremque laudantium, totam rem aperiam, eaque ipsa quae ab illo inventore veritatis et quasi architecto beatae vitae dicta sunt explicabo. Nemo enim ipsam voluptatem quia voluptas sit aspernatur aut odit aut fugit, sed quia consequuntur magni dolores eos qui ratione voluptatem sequi nesciunt.</p>
    <a class="btn" href="#">READ MORE</a>
  </article>
</section>

<section class="why">
  <h2 class="abs section-title" style="top:58px">WHY CHOOSE US</h2>
  <div class="abs section-rule" style="top:112px"></div>

  <div class="abs feature-icon" style="left:131px;top:182px"><svg width="38" height="38" viewBox="0 0 24 24" fill="none" stroke="#fff" stroke-width="1.8"><circle cx="12" cy="12" r="8"/><path d="M8 12l3 3 5-6"/></svg></div>
  <div class="abs feature" style="left:224px;top:181px"><h4>QUALITY</h4><p>Sed ut perspiciatis unde omnis iste natus error sit voluptatem accusantium dolorem.</p></div>

  <div class="abs feature-icon" style="left:131px;top:295px"><svg width="34" height="34" viewBox="0 0 24 24" fill="none" stroke="#fff" stroke-width="1.8"><path d="M5 3h4l2 5-2.5 1.5a11 11 0 0 0 6 6L16 13l5 2v4a2 2 0 0 1-2 2A16 16 0 0 1 3 5a2 2 0 0 1 2-2z"/></svg></div>
  <div class="abs feature" style="left:224px;top:294px"><h4>SUPPORT</h4><p>Sed ut perspiciatis unde omnis iste natus error sit voluptatem accusantium dolorem.</p></div>

  <div class="abs feature-icon" style="left:131px;top:414px"><svg width="32" height="32" viewBox="0 0 24 24" fill="#fff"><rect x="3" y="10" width="4" height="11"/><path d="M9 10l4-7c2 0 2.5 1.5 2 4h5a2 2 0 0 1 2 2l-2 10a2 2 0 0 1-2 2H9z"/></svg></div>
  <div class="abs feature" style="left:224px;top:413px"><h4>SATISFACTION</h4><p>Sed ut perspiciatis unde omnis iste natus error sit voluptatem accusantium dolorem.</p></div>

  <div class="abs globe" role="img" aria-label="Globe with a red arrow circling it"></div>

  <div class="abs feature" style="left:783px;top:181px"><h4>WORLDWIDE SHIPPING</h4><p>Sed ut perspiciatis unde omnis iste natus error sit voluptatem accusantium dolorem.</p></div>
  <div class="abs feature-icon" style="left:1000px;top:182px"><svg width="38" height="38" viewBox="0 0 24 24" fill="none" stroke="#fff" stroke-width="1.6"><circle cx="12" cy="12" r="9"/><ellipse cx="12" cy="12" rx="4" ry="9"/><path d="M3 12h18M5 7h14M5 17h14"/></svg></div>

  <div class="abs feature" style="left:783px;top:294px"><h4>SECURE</h4><p>Sed ut perspiciatis unde omnis iste natus error sit voluptatem accusantium dolorem.</p></div>
  <div class="abs feature-icon" style="left:1000px;top:295px"><svg width="30" height="30" viewBox="0 0 24 24" fill="#fff"><path d="M7 10V7a5 5 0 0 1 10 0v3h-2V7a3 3 0 0 0-6 0v3z"/><rect x="5" y="10" width="14" height="11" rx="1"/><circle cx="12" cy="15" r="1.8" fill="#2c3246"/></svg></div>

  <div class="abs feature" style="left:783px;top:413px"><h4>BENEFITS</h4><p>Sed ut perspiciatis unde omnis iste natus error sit voluptatem accusantium dolorem.</p></div>
  <div class="abs feature-icon" style="left:1000px;top:414px"><svg width="38" height="38" viewBox="0 0 24 24" fill="none" stroke="#fff" stroke-width="1.6"><circle cx="12" cy="12" r="9"/><circle cx="12" cy="10" r="3"/><path d="M6.5 18a6 6 0 0 1 11 0"/></svg></div>
</section>

<section class="benefits">
  <h2 class="abs section-title" style="top:44px">BENEFITS</h2>
  <div class="abs section-rule" style="top:98px"></div>
  <div class="abs benefit-list">
    <article class="benefit-card">
      <svg viewBox="0 0 48 44" fill="none" stroke="#2c3246" stroke-width="2"><path d="M4 42h40"/><rect x="8" y="28" width="6" height="14"/><rect x="18" y="22" width="6" height="20"/><rect x="28" y="26" width="6" height="16"/><rect x="38" y="16" width="6" height="26"/><path d="M8 18l10-8 10 6 12-10" stroke="#ee2f2f"/></svg>
      <h4>LOREM IPSUM DOLOR</h4>
      <p>Sed ut perspiciatis unde om nis iste natus error sit volu ptatem accusantium dolor emque laud antium, totam rem. aliquip ex ea com modo consequat</p>
    </article>
    <article class="benefit-card">
      <svg viewBox="0 0 48 44" fill="none" stroke="#2c3246" stroke-width="2"><path d="M24 2l16 6v12c0 11-7 18-16 22C15 38 8 31 8 20V8z"/><path d="M17 22l5 5 9-10" stroke="#ee2f2f"/></svg>
      <h4>LOREM IPSUM DOLOR</h4>
      <p>Sed ut perspiciatis unde om nis iste natus error sit volu ptatem accusantium dolor emque laud antium, totam rem. aliquip ex ea com modo consequat</p>
    </article>
    <article class="benefit-card">
      <svg viewBox="0 0 48 44" fill="none" stroke="#2c3246" stroke-width="2"><path d="M6 6h7l3 8-4 3a18 18 0 0 0 9 9l3-4 8 3v7a3 3 0 0 1-3 3A28 28 0 0 1 3 9a3 3 0 0 1 3-3z"/><rect x="26" y="2" width="18" height="13" rx="2" stroke="#ee2f2f"/><path d="M30 7h10M30 11h6" stroke="#ee2f2f"/></svg>
      <h4>LOREM IPSUM DOLOR</h4>
      <p>Sed ut perspiciatis unde om nis iste natus error sit volu ptatem accusantium dolor emque laud antium, totam rem. aliquip ex ea com modo consequat</p>
    </article>
    <article class="benefit-card">
      <svg viewBox="0 0 48 44" fill="none" stroke="#2c3246" stroke-width="2"><path d="M34 14V2H8v40h26v-8"/><path d="M13 9h16M13 15h4M20 15h9M13 21h4M20 21h9M13 27h4M20 27h9"/><path d="M26 24h18M39 19l5 5-5 5" stroke="#ee2f2f"/></svg>
      <h4>LOREM IPSUM DOLOR</h4>
      <p>Sed ut perspiciatis unde om nis iste natus error sit volu ptatem accusantium dolor emque laud antium, totam rem. aliquip ex ea com modo consequat</p>
    </article>
  </div>
</section>

<footer class="site-footer">
  <div class="abs brand-mark" style="left:134px;top:57px"></div>
  <div class="abs brand-name" style="left:217px;top:74px;color:var(--white)">MIRADOR</div>

  <div class="abs footer-col" style="left:460px;top:52px">
    <h5>MENU</h5>
    <ul class="footer-menu"><li>HOME</li><li>ABOUT US</li><li>SERVICES</li><li>BLOG</li><li>CONTACT US</li></ul>
  </div>

  <div class="abs footer-col" style="left:654px;top:52px">
    <h5>CONTACT US</h5>
    <div class="footer-item"><span class="ico"><svg width="14" height="14" viewBox="0 0 24 24" fill="#2c3246"><path d="M12 2a7 7 0 0 0-7 7c0 5 7 13 7 13s7-8 7-13a7 7 0 0 0-7-7zm0 9.5A2.5 2.5 0 1 1 12 6.5a2.5 2.5 0 0 1 0 5z"/></svg></span><span>4120 Sierra Vista Road<br>Quito 170150</span></div>
    <div class="footer-item"><span class="ico"><svg width="13" height="13" viewBox="0 0 24 24" fill="#2c3246"><path d="M5 3h4l2 5-2.5 1.5a11 11 0 0 0 6 6L16 13l5 2v4a2 2 0 0 1-2 2A16 16 0 0 1 3 5a2 2 0 0 1 2-2z"/></svg></span><span>Call Us<br>555.014.2200</span></div>
    <div class="footer-item"><span class="ico"><svg width="13" height="13" viewBox="0 0 24 24" fill="#2c3246"><path d="M2 5h20v14H2z"/><path d="M2 5l10 8 10-8" stroke="#fff" stroke-width="2" fill="none"/></svg></span><span>E mail Us<br>info@miradorexport.com</span></div>
  </div>

  <div class="abs footer-col" style="left:940px;top:52px">
    <h5>FOLLOW US</h5>
    <div class="footer-item"><span class="ico"></span><span>Like us on<br>PAGEHUB</span></div>
    <div class="footer-item"><span class="ico"></span><span>Follow us on<br>CHIRPLY</span></div>
    <div class="footer-item"><span class="ico"></span><span>Follow us on<br>LINKWORK</span></div>
  </div>

  <div class="abs footer-rule"></div>
  <p class="abs copyright">Copyright © 2020 All Rights Reserved</p>
</footer>

</body>
</html>
```